Health - Quiet Meadow Project

I am running a new Quiet Meadow Conference that will have meditation, mediums and healers - this is a first time conference. However the conference is aimed at mainstream 'normal' people. The 'normal' people, don't want to hear or see words like Tantra, Prana, Angels, etc, but they have problems that can be alleviated through these mediums. The design should communicate light, soothing, comforting, healing. I would like a web design for a single page that can be used as a landing page for the conference registration. I also need a logo and a flyer that can be made into posters A4 or A3 posters. I need to be able to edit all documents as there will be changes in the program through time. I have attached the initial agenda. This conference will be held in Victoria, Australia.
Target Market(s)
Mums and grandmas
Industry/Entity Type
Health And Wellness
Number of Pages Required
1 page
Look and feel
Each slider illustrates characteristics of the customer's brand and the style your logo design should communicate.

```html
<!DOCTYPE html>
<html lang="en">
<head>
<meta charset="utf-8">
<title>Quiet Meadow Conference – Registration</title>
<link href="https://fonts.googleapis.com/css2?family=Lato:wght@400;700;900&display=swap" rel="stylesheet">
<style>
:root{
  --navy:#1b5a86;
  --green:#8cc63f;
  --green-dark:#6a9e25;
  --ink:#222;
  --muted:#666;
  --line:#c9c9c9;
  --panel:#f1f1f1;
  --dark:#2a2622;
  --pin:#1b5a86;
  --phone:#6cc7c9;
  --mail:#8cc63f;
}
*{box-sizing:border-box;margin:0;padding:0}
html,body{width:1200px;height:3346px;overflow:hidden}
body{font-family:'Lato',sans-serif;color:var(--ink);background:#fff;position:relative}

/* header */
.site-header{position:absolute;left:0;top:0;width:1200px;height:115px;background:linear-gradient(#fff,#f3f3f3)}
.social{position:absolute;display:flex;gap:8px}
.social span{width:30px;height:30px;border-radius:50%;display:block}
.social .s1{background:#3b5998}.social .s2{background:#55acee}.social .s3{background:#0e76a8}.social .s4{background:#dd4b39}
.header-social{left:53px;top:40px}
.brand{position:absolute;left:0;width:1200px;top:30px;text-align:center;font-size:40px;font-weight:700;color:var(--navy)}
.brand .dot{display:inline-block;width:14px;height:14px;border-radius:50%;background:var(--green);margin-right:10px;vertical-align:middle}
.btn-register{position:absolute;left:970px;top:40px;width:178px;height:38px;background:var(--green);color:#fff;font-size:17px;font-weight:700;display:flex;align-items:center;padding-left:22px;border-radius:2px}
.btn-register .arrow{position:absolute;right:0;top:0;width:36px;height:38px;background:var(--green-dark);display:flex;align-items:center;justify-content:center}

/* hero */
.hero{position:absolute;left:0;top:115px;width:1200px;height:577px;background:linear-gradient(180deg,#a9c7e3 0%,#c8dced 38%,#4f8fbf 55%,#1f6aa3 80%,#2f5f82 100%)}
.hero-figure{position:absolute;left:720px;top:0;width:480px;height:577px;background:linear-gradient(90deg,rgba(235,225,215,0),rgba(240,232,225,.75) 40%,rgba(110,90,75,.7) 95%)}
.hero h1{position:absolute;left:53px;top:302px;font-size:44px;font-weight:700;color:var(--navy)}
.hero p{position:absolute;left:53px;top:366px;font-size:21px;font-weight:700;color:#111}
.hero .btn-register{left:53px;top:417px;width:198px}
.dots{position:absolute;left:55px;top:480px;display:flex;gap:5px}
.dots span{width:11px;height:11px;border-radius:50%;background:#fff}
.dots span:first-child{background:var(--green)}

/* section titles */
.title{position:absolute;left:0;width:1200px;text-align:center;font-size:33px;font-weight:700;color:var(--navy)}
.title em{font-style:normal;color:var(--green)}
.divider{position:absolute;left:375px;width:450px;height:30px}

/* welcome */
.welcome p{position:absolute;left:60px;top:845px;width:1080px;text-align:center;font-size:16px;line-height:25px;color:#333}

/* speakers */
.speakers{position:absolute;left:0;top:975px;width:1200px;height:1133px;background:linear-gradient(135deg,#f6f6f6,#ececec)}
.card{position:absolute;left:53px;width:1094px;border:2px solid var(--line);border-radius:24px;background:rgba(255,255,255,.6)}
.card.active{border-color:#bfd98e}
.avatar{position:absolute;left:30px;top:28px;width:90px;height:90px;border-radius:50%;border:4px solid #fff;box-shadow:0 0 0 1px #ddd}
.card-body{position:absolute;left:180px;right:28px;top:22px;border-left:1px solid #ddd;padding-left:0}
.card-body .inner{margin-left:0;padding-left:0}
.facil{font-size:15px;font-weight:700;color:var(--navy);display:flex;align-items:center;gap:8px}
.time{background:var(--green);color:#111;border-radius:10px;padding:1px 8px;font-size:14px}
.topic{font-size:13px;font-weight:700;margin:6px 0 6px}
.card-body p{font-size:12.5px;line-height:19px;color:#222;margin-bottom:8px}
.more{color:var(--green-dark)}

/* registration */
.register{position:absolute;left:0;top:2108px;width:1200px;height:528px;background:linear-gradient(180deg,#3a3630,#2c2823 60%,#1e1b18)}
.register .title{color:#fff}
.field{position:absolute;border:1px solid #777;background:rgba(255,255,255,.05);color:#bbb;font-size:13px;padding:14px 14px}
.submit{position:absolute;left:493px;top:2536px;width:214px;height:46px;background:linear-gradient(#8cc63f,#5f9322);color:#fff;font-size:19px;font-weight:900;letter-spacing:1px;display:flex;align-items:center;justify-content:center}

/* contact */
.contact-item{position:absolute;width:300px;text-align:center}
.contact-item .icon{width:103px;height:103px;border-radius:50%;margin:0 auto;display:flex;align-items:center;justify-content:center}
.contact-item h3{margin-top:38px;font-size:17px;font-weight:900;color:#222}
.contact-item p{margin-top:14px;font-size:15px;color:var(--muted)}

/* map */
.map{position:absolute;left:0;top:2921px;width:1200px;height:284px;background:linear-gradient(135deg,#e9e2d2,#efe6d6 50%,#e3d9c4)}
.map-label{position:absolute;left:432px;top:3025px;width:158px;height:56px;background:#fff;box-shadow:0 1px 4px rgba(0,0,0,.3);display:flex;align-items:center;justify-content:center;font-size:19px;font-weight:700;color:var(--navy)}
.map-pin{position:absolute;left:492px;top:3088px}

/* footer */
.copyright{position:absolute;left:0;top:3236px;width:1200px;text-align:center;font-size:14px;color:#222}
.footer-social{left:525px;top:3276px}
</style>
</head>
<body>

<header class="site-header">
  <div class="social header-social"><span class="s1"></span><span class="s2"></span><span class="s3"></span><span class="s4"></span></div>
  <div class="brand"><span class="dot"></span>Quiet Meadow</div>
  <div class="btn-register">Register Now<span class="arrow"><svg width="16" height="16" viewBox="0 0 16 16"><path d="M3 3l5 5-5 5M8 3l5 5-5 5" fill="none" stroke="#fff" stroke-width="2"/></svg></span></div>
</header>

<section class="hero">
  <div class="hero-figure" role="img" aria-label="Woman in white meditating with palms together on rocks by the sea"></div>
  <h1>Life Up Your Spirit</h1>
  <p>Treating,body &amp; Spirit to Promote Confidence in Recovery</p>
  <div class="btn-register">Register Now<span class="arrow"><svg width="16" height="16" viewBox="0 0 16 16"><path d="M3 3l5 5-5 5M8 3l5 5-5 5" fill="none" stroke="#fff" stroke-width="2"/></svg></span></div>
  <div class="dots"><span></span><span></span><span></span><span></span></div>
</section>

<section class="welcome">
  <h2 class="title" style="top:736px">Welcome to Quiet Meadow</h2>
  <svg class="divider" style="top:795px" viewBox="0 0 450 30"><line x1="0" y1="15" x2="450" y2="15" stroke="#ccc"/><circle cx="225" cy="15" r="7" fill="#fff" stroke="#8cc63f" stroke-width="3"/></svg>
  <p>Sed ut perspiciatis unde omnis iste natus error sit voluptatem accusantium dolo remque laudantium, totam rem aperiam, eaque ipsa quae ab illo inventore veritatis et quasi architecto beatae vitae dicta sunt explicabo. Sed ut perspiciatis unde omnis iste natus error sit voluptatem accusantium dolo. Sed ut perspiciatis unde omnis iste natus error sit voluptatem accusantium dolo.</p>
</section>

<section class="speakers">
  <h2 class="title" style="top:48px">Our <em>Speakers</em></h2>
  <svg class="divider" style="top:106px" viewBox="0 0 450 30"><line x1="0" y1="15" x2="450" y2="15" stroke="#ccc"/><circle cx="225" cy="15" r="7" fill="#fff" stroke="#8cc63f" stroke-width="3"/></svg>
</section>

<article class="card active" style="top:1138px;height:374px">
  <div class="avatar" role="img" aria-label="Portrait of the facilitator" style="background:linear-gradient(#a0583a,#e0b59a)"></div>
  <div class="card-body">
    <div class="facil" style="padding-left:14px">Facilitator: Maren Ashby <span class="time">(Time: 9:00 – 10:45)</span></div>
    <div style="padding-left:14px">
    <div class="topic">Wild Hairs – Embarking Upon the Spiritual Life</div>
    <p>Everyone Is Searching For Love, Joy And Peace – Aren't We? Yet Love, Joy And Peace Is Already Our Natural State Of Being. So How Did We Come To Forget This Fundamental Truth? Why Are We Searching For What We Already Are? The Answers To These Questions Are Rather Simple And Obvious, But Only After We Come To Understand The Nature Of The Human Ego. For Too Long, The Human Ego Has Taken Us On A Wild Goose Chase.</p>
    <p>It Could Take An Entire Lifetime Of Study, To Fully Grasp The Magnitude Of The Nature Of Awakening. In This Discussion You Will Receive A Very Simple To Understand Explanation Of The Journey Humanity Is Undertaking, From Conception To Enlightenment – And How You Can Assess Where You Are On Your Own Journey And Keys To Unlocking Your Love, Joy And Peace.</p>
    <p>A Modern Day Spiritual Facilitator, Maren Ashby, Takes A Fresh And Fun Approach To Redefining Spirituality For Everyone. Maren's Own Spiritual Awakening Propelled Her To Share What Is Possible, When One Truly Commits To Transformation. True Transformation Requires A Deep Understanding Of Our Mind. Hidden Deep Within Our Mind-made Stories Lies, In Waiting, The Truth Of Who We Are. Maren Is An Ordained Minister, Author, Certified Clinical Hypnotherapist, Ministerial Counselor, Workshop Facilitator, Speaker And Medical Intuitive. Her Simple Techniques And Practical Tools Have Helped To Transform Many Lives.</p>
    </div>
  </div>
</article>

<article class="card" style="top:1539px;height:149px">
  <div class="avatar" role="img" aria-label="Portrait of the facilitator" style="top:26px;background:linear-gradient(#b06a3a,#f0d0b0)"></div>
  <div class="card-body" style="top:20px">
    <div style="padding-left:14px">
    <div class="facil">Facilitator: Tessa Rowan <span class="time">(Time: 11:00 – 12:45)</span></div>
    <div class="topic" style="margin:3px 0 2px">Conscious Connection &amp; Living Life Fully</div>
    <p>We Live In A World Where Most People Feel Disconnected Or 'out Of Synch' With Friends, Loved Ones And The Daily Experiences We Share With One Another. This Workshop Is Designed To Offer You A Framework For LIVING More Consciously, Intimately And With Greater Connection, Presence And Depth – To Ourselves And Others. The More We Feel Connected To Ourselves, The More Connected...<span class="more">[+]</span></p>
    </div>
  </div>
</article>

<article class="card" style="top:1717px;height:152px">
  <div class="avatar" role="img" aria-label="Portrait of the facilitator" style="top:28px;background:linear-gradient(#6d9bc4,#d8b49a)"></div>
  <div class="card-body" style="top:20px">
    <div style="padding-left:14px">
    <div class="facil">Facilitator: Owen Hale <span class="time">(Time: 1:30 – 3:15)</span></div>
    <div class="topic" style="margin:3px 0 2px">The Slow Breath to Freedom</div>
    <p>Stress is is one of the number one causes of leading diseases today. The connection between Mind and Body has long since been established by both science and spirituality. This session will guide you through simple meditations, self-inquiry, mindful eating and movement. You will find these tools extremely useful to releasing the stress valve, improving your relationships and managing your<span class="more">[+]</span></p>
    </div>
  </div>
</article>

<article class="card" style="top:1898px;height:149px">
  <div class="avatar" role="img" aria-label="Portrait of the facilitator" style="top:26px;background:linear-gradient(#4d5a3a,#b89a80)"></div>
  <div class="card-body" style="top:20px">
    <div style="padding-left:14px">
    <div class="facil">Facilitator: Nadia Brooks <span class="time">(Time: 3:30 – 5:00)</span></div>
    <div class="topic" style="margin:3px 0 2px">Learning to SHINE</div>
    <p>In a world where too often we feel less than our bright, shiny best we can all afford to bring out more of our own natural light to shine for ourselves and others. In this session, Nadia will guide you through ways to connect with your inner SHINE and not only use that to brighten yourself, but to shine your light on others to share in warmth and love that improves all things.<span class="more">[+]</span></p>
    </div>
  </div>
</article>

<section class="register" role="img" aria-label="Silhouette of a person meditating at dusk">
  <h2 class="title" style="top:46px">Registration <em>Form</em></h2>
  <svg class="divider" style="top:104px" viewBox="0 0 450 30"><line x1="0" y1="15" x2="450" y2="15" stroke="#666"/><circle cx="225" cy="15" r="7" fill="none" stroke="#8cc63f" stroke-width="3"/></svg>
</section>
<div class="field" style="left:53px;top:2277px;width:531px;height:47px">Name</div>
<div class="field" style="left:616px;top:2277px;width:531px;height:47px">Email</div>
<div class="field" style="left:53px;top:2334px;width:531px;height:47px">Phone</div>
<div class="field" style="left:616px;top:2334px;width:531px;height:47px">Time</div>
<div class="field" style="left:53px;top:2391px;width:1094px;height:110px">Message</div>
<div class="submit">SUBMIT</div>

<div class="contact-item" style="left:122px;top:2680px">
  <div class="icon" style="background:var(--pin)"><svg width="40" height="52" viewBox="0 0 40 52"><path d="M20 2C10 2 3 9 3 19c0 12 17 31 17 31s17-19 17-31C37 9 30 2 20 2z" fill="#fff"/><circle cx="20" cy="19" r="6" fill="#1b5a86"/></svg></div>
  <h3>LOCATION:</h3><p>85 Lorem ipsum dolor, ONK1S0T7</p>
</div>
<div class="contact-item" style="left:483px;top:2680px">
  <div class="icon" style="background:var(--phone)"><svg width="46" height="46" viewBox="0 0 24 24"><path d="M6.6 10.8a15 15 0 006.6 6.6l2.2-2.2a1 1 0 011-.25 11.4 11.4 0 003.6.57 1 1 0 011 1V20a1 1 0 01-1 1A17 17 0 013 4a1 1 0 011-1h3.5a1 1 0 011 1c0 1.25.2 2.45.57 3.57a1 1 0 01-.25 1z" fill="#fff"/></svg></div>
  <h3>PHONE:</h3><p>+123-456-7890</p>
</div>
<div class="contact-item" style="left:813px;top:2680px">
  <div class="icon" style="background:var(--mail)"><svg width="50" height="36" viewBox="0 0 50 36"><rect x="1" y="1" width="48" height="34" fill="#fff"/><path d="M1 1l24 19L49 1" fill="none" stroke="#8cc63f" stroke-width="3"/></svg></div>
  <h3>EMAIL:</h3><p>info@quietmeadow.org</p>
</div>

<div class="map" role="img" aria-label="Road map of the venue region in South Australia"></div>
<div class="map-label">Quiet Meadow</div>
<svg class="map-pin" width="36" height="48" viewBox="0 0 40 52"><path d="M20 2C10 2 3 9 3 19c0 12 17 31 17 31s17-19 17-31C37 9 30 2 20 2z" fill="#222"/><circle cx="20" cy="19" r="7" fill="#fff"/></svg>

<footer>
  <p class="copyright">Copyright © 2016 Quiet Meadow . All Rights Reserved.</p>
  <div class="social footer-social"><span class="s1"></span><span class="s2"></span><span class="s3"></span><span class="s4"></span></div>
</footer>

</body>
</html>
```